Small Machinery Hire Company Needs Coaster Design

Please design an eye catching coaster/sticker to place in local pubs and restaurants. Please use our attached logo and incorporate our rustic earthy feel into the colours. Use the following details. Definite want the focus to be on the logo and phone number.

Would appreciate if it could be multi-purpose as a basic sign as well.

Dry/Wet Hire Available
Ph: 0451207964

(Use FaceBook icon) fernbook.net/marrowbrookplanthire2917/

Target Market(s)

At homer DIY-ers. Middle class men who would like to hire a machine to work on their own pride and joy home.

Industry/Entity Type

Construction Company

Font styles to use
Other font styles liked:
• Something that matches the Logo

Colors
fefdec
ec1f27
474747
919191

Requirements
Nice to have
• Preferably a square shape so the it is more multi purpose

```html
<!DOCTYPE html>
<html lang="en">
<head>
<meta charset="utf-8">
<title>Marrowbrook Plant Hire – Coaster</title>
<link rel="stylesheet" href="https://fonts.googleapis.com/css2?family=Source+Sans+3:wght@400;600&display=swap">
<style>
  :root {
    --page-bg: #ffffff;
    --coaster-fill: #fddf80;
    --coaster-edge: #2b2b2b;
    --frame-line: #111111;
    --ink: #141414;
    --brand-red: #7e1a17;
    --emblem-tone: #bfa876;
    --texture-tone: #efcf72;
    --social-mark: #ffffff;
  }
  html, body {
    margin: 0;
    padding: 0;
    width: 1200px;
    height: 758px;
    overflow: hidden;
    background: var(--page-bg);
  }
  .canvas {
    position: relative;
    width: 1200px;
    height: 758px;
  }
  .coaster {
    position: absolute;
    left: 358px;
    top: 127px;
    width: 498px;
    height: 470px;
    box-sizing: border-box;
    border: 1.5px solid var(--coaster-edge);
    border-radius: 22px;
    background:
      radial-gradient(circle at 30% 75%, var(--texture-tone) 0%, transparent 60%),
      radial-gradient(circle at 75% 30%, var(--texture-tone) 0%, transparent 55%),
      var(--coaster-fill);
    overflow: hidden;
  }
  .frame {
    position: absolute;
    left: -1.5px;
    top: -1.5px;
    width: 498px;
    height: 470px;
  }
  .emblem-area {
    position: absolute;
    left: 147px;
    top: 51px;
    width: 178px;
    height: 250px;
    border-radius: 40% 40% 48% 48%;
    background: linear-gradient(180deg, var(--emblem-tone) 0%, rgba(191,168,118,0.25) 100%);
    opacity: 0.6;
  }
  .contact {
    position: absolute;
    left: 0;
    top: 30px;
    width: 100%;
    text-align: center;
    font-family: "Source Sans 3", sans-serif;
    color: var(--ink);
  }
  .contact__service,
  .contact__phone {
    font-size: 27px;
    line-height: 33px;
    font-weight: 400;
  }
  .contact__social {
    display: inline-flex;
    align-items: center;
    gap: 9px;
    margin-top: 2px;
    font-size: 14.5px;
  }
  .contact__social-mark {
    width: 26px;
    height: 26px;
    background: var(--social-mark);
  }
  .brand-name {
    position: absolute;
    left: 0;
    width: 100%;
    text-align: center;
    font-family: "Source Sans 3", sans-serif;
    font-weight: 600;
    text-transform: uppercase;
    color: var(--brand-red);
    white-space: nowrap;
  }
  .brand-name__main {
    top: 318px;
    font-size: 40px;
    line-height: 48px;
    letter-spacing: 1px;
  }
  .brand-name__sub {
    top: 430px;
    font-size: 24px;
    line-height: 30px;
    letter-spacing: 3px;
  }
</style>
</head>
<body>
  <div class="canvas">
    <div class="coaster">
      <svg class="frame" viewBox="0 0 498 470" aria-hidden="true">
        <path d="M120 451.5 H39.5 A18 18 0 0 1 21.5 433.5 V38.5 A18 18 0 0 1 39.5 20.5 H458.5 A18 18 0 0 1 476.5 38.5 V433.5 A18 18 0 0 1 458.5 451.5 H374"
              fill="none" stroke="var(--frame-line)" stroke-width="3"/>
      </svg>
      <div class="emblem-area" role="img" aria-label="Faint large animal head emblem decoration"></div>
      <div class="contact">
        <div class="contact__service">Dry/Wet Hire Available</div>
        <div class="contact__phone">0451207964</div>
        <div class="contact__social">
          <span class="contact__social-mark"></span>
          <span>fernbook.net/marrowbrookplanthire2917/</span>
        </div>
      </div>
      <div class="brand-name brand-name__main">Marrowbrook</div>
      <div class="brand-name brand-name__sub">Plant Hire</div>
    </div>
  </div>
</body>
</html>
```